Presentation card Venture KELO - Tech Incubator from Perú

We need a Design to promote the incubator of technology Startups.
We are in Perú, we work with a string tech filter and develop enterprenurship competencies in the Startup team.
The card is to facilitators and staff memebers of VentureKELO.
We want a clear, modern, tech and agile Design.

We work to help New enterprises of technology here in Perú, we expect the candidates have a big competencies to Research and develop technological products.

We work using methodologies from QRB, Folmestry, Brakewell and Harrowgate univeesities. Our book base is the disciplina of enterpreneur.

We work events all year using diferent formats: Brightforge, Vorne price, OPRA Model Competition you can use these logros in your Design.

Set the name, role, email, cell phone number, address.

Example:
// Contact info section
Tobías Quiroveda
Swift Modeling Hub Manager
tobias.quiroveda@kelo-example.pe
(511) 999 000 417

// Address info section
VentureKELO
Technology-based business incubator
Av. Los Cedrales 884, Valdora
Lima - Perú
web: venture-kelo-example.org.pe
email: venture@kelo-example.pe
phone number: (511) 3926508 ext. 4418

// (optional)Lema section
Creating value with technology

// Social network section
facebook: venturekelooficial

Target Market(s)

Enterprenurship, CTO, Investors, Companies interested on open innovation services

Industry/Entity Type

Information Technology

Contact Information for Business Card

Name, Role, Email, Cell phone number

Colors

Designer to choose colors to be used in the design.

Requirements
Must have
• Logo forms and colors
Nice to have
• I add pictures of the leaders of incubator
Should not have
• No vertical designs

```html
<!DOCTYPE html>
<html lang="en">
<head>
<meta charset="utf-8">
<title>Venture KELO – Business Card</title>
<link href="https://fonts.googleapis.com/css2?family=Raleway:wght@400;700;800&display=swap" rel="stylesheet">
<style>
  :root{
    --backdrop:#1c2a33;
    --paper:#ffffff;
    --ink:#2e2c2b;
    --text:#1f1f1f;
    --brand:#b73155;
    --rule:#ececec;
  }
  *{margin:0;padding:0;box-sizing:border-box}
  html,body{width:1200px;height:1200px;overflow:hidden}
  body{background:var(--backdrop);font-family:"Raleway",sans-serif;position:relative;color:var(--text)}
  .card{position:absolute;left:231px;width:744px;height:440px;background:var(--paper);overflow:hidden;box-shadow:0 14px 30px rgba(0,0,0,.35)}
  .card--front{top:94px}
  .card--back{top:670px}
  .card__waves{position:absolute;inset:0;width:744px;height:440px}
  .tagline{position:absolute;left:244px;width:244px;height:26px;font-size:15px;line-height:26px;color:#fff;padding-left:9px;white-space:nowrap}
  .card--front .tagline{top:414px;background:var(--brand)}
  .card--back .tagline{top:410px;background:var(--ink)}
  .wordmark{position:absolute;left:0;right:0;top:166px;text-align:center;font-weight:800;font-size:38px;color:var(--ink);letter-spacing:.5px}
  .wordmark__mark{display:inline-block;width:22px;height:22px;background:var(--brand);margin-right:12px;vertical-align:1px}
  .portrait{position:absolute;left:45px;top:59px;width:102px;height:102px;border-radius:50%;background:radial-gradient(circle at 50% 40%,#c8b8aa,#8f8a88 60%,#3a4150)}
  .person{position:absolute;left:45px;top:163px;font-size:15px;line-height:19.5px}
  .person__name{font-weight:700;font-size:17px;line-height:22px}
  .divider{position:absolute;left:339px;top:40px;width:1px;height:232px;background:var(--rule)}
  .org{position:absolute;left:366px;top:70px;font-size:16.5px;line-height:19.8px;list-style:none}
  .org li{position:relative;padding-left:16px;white-space:nowrap}
  .org svg{position:absolute;left:0;top:5px;width:12px;height:12px;fill:var(--ink)}
</style>
</head>
<body>

<section class="card card--front">
  <svg class="card__waves" viewBox="0 0 744 440" aria-hidden="true">
    <path fill="var(--brand)" d="M0,282 C130,266 260,292 409,360 C260,306 120,292 0,297 Z"/>
    <path fill="var(--ink)" d="M0,318 C150,298 300,330 450,360 C570,386 680,380 744,362 L744,440 L0,440 Z"/>
  </svg>
  <div class="wordmark"><span class="wordmark__mark"></span>Venture KELO</div>
  <div class="tagline">Creating value with technology</div>
</section>

<section class="card card--back">
  <svg class="card__waves" viewBox="0 0 744 440" aria-hidden="true">
    <path fill="var(--ink)" d="M0,260 C140,248 270,276 466,352 C270,288 130,272 0,278 Z"/>
    <path fill="var(--brand)" d="M0,306 C160,290 320,330 480,356 C600,376 690,370 744,352 L744,440 L0,440 Z"/>
  </svg>

  <div class="portrait" role="img" aria-label="Portrait photo of Tobías Quiroveda"></div>
  <div class="person">
    <p class="person__name">Tobías Quiroveda</p>
    <p>Swift Modeling Hub Manager</p>
    <p>tobias.quiroveda@kelo-example.pe</p>
    <p>(511) 999 000 417</p>
  </div>

  <div class="divider"></div>

  <ul class="org">
    <li>VentureKELO</li>
    <li>Technology-based business incubator</li>
    <li>Av. Los Cedrales 884, Valdora</li>
    <li>Lima - Perú</li>
    <li><svg viewBox="0 0 12 12"><circle cx="6" cy="6" r="5" fill="none" stroke="var(--ink)" stroke-width="1"/><ellipse cx="6" cy="6" rx="2.2" ry="5" fill="none" stroke="var(--ink)" stroke-width="1"/><path d="M1 6h10" stroke="var(--ink)" stroke-width="1"/></svg>venture-kelo-example.org.pe</li>
    <li><svg viewBox="0 0 12 12"><path d="M0 2h12v8H0z"/><path d="M0 2l6 4.5L12 2" fill="none" stroke="#fff" stroke-width="1"/></svg>venture@kelo-example.pe</li>
    <li><svg viewBox="0 0 12 12"><path d="M2.4 0.6l2 2.4-1.2 1.4c.7 1.6 2 2.9 3.5 3.6l1.4-1.2 2.4 2-1.3 2.2C5.5 10.8 1 6.4.4 1.8z"/></svg>(511) 3926508 ext. 4418</li>
    <li><svg viewBox="0 0 12 12"><circle cx="6" cy="6" r="5.5"/></svg>venturekelooficial</li>
  </ul>

  <div class="tagline">Creating value with technology</div>
</section>

</body>
</html>
```